New business card design to go with our new logo

just want an eye-catching business card to go with our new logo. We are open to double sided or single sided. Just want it to have the following info on it. Whatever layout you think looks best.

First and Last Name
Title
Phone 801-555-0187
Address 312 W. Larkmoor Avenue Orem UT 84057
Email thecrew@meadowstailandkennel.example

Industry/Entity Type

Business

```html
<!DOCTYPE html>
<html lang="en">
<head>
<meta charset="utf-8">
<title>Meadow's Tail &amp; Kennel — Business Card</title>
<link rel="stylesheet" href="https://fonts.googleapis.com/css2?family=Libre+Baskerville:ital,wght@0,400;0,700;1,400&display=swap">
<style>
  :root {
    --bg: #3a3a3a;
    --card: #ffffff;
    --card-shade: #f1f1f1;
    --orange: #ef8a45;
    --blue: #2a9fd6;
    --band: #86c3d6;
    --badge: #4ba7c0;
    --ink: #333333;
    --icon: #1f2a33;
  }
  * { margin: 0; padding: 0; box-sizing: border-box; }
  html, body { width: 1200px; height: 900px; overflow: hidden; }
  body {
    background: var(--bg);
    font-family: "Libre Baskerville", Georgia, serif;
    color: var(--ink);
    position: relative;
  }
  .card {
    position: absolute;
    left: 280px;
    width: 640px;
    height: 366px;
    border-radius: 26px;
    background: linear-gradient(180deg, var(--card) 60%, var(--card-shade));
    overflow: hidden;
  }
  .card--front { top: 50px; }
  .card--back { top: 470px; }

  /* Company name */
  .brand {
    position: absolute;
    color: var(--orange);
    font-weight: 700;
    white-space: nowrap;
  }
  .card--front .brand {
    left: 0; right: 0; top: 160px;
    text-align: center;
    font-size: 36px;
  }
  .card--back .brand {
    right: 40px; top: 72px;
    font-size: 22px;
  }

  /* Back side */
  .person { position: absolute; left: 50px; top: 140px; }
  .person__name { color: var(--orange); font-size: 23px; }
  .person__title { color: var(--blue); font-style: italic; font-size: 15px; margin-top: 4px; }

  .contacts { position: absolute; left: 50px; top: 218px; list-style: none; font-size: 15px; line-height: 22px; }
  .contacts li { display: flex; align-items: center; gap: 8px; white-space: nowrap; }
  .contacts svg { width: 14px; height: 14px; flex: none; }

  .band {
    position: absolute; left: 0; right: 0; bottom: 0; height: 76px;
    background: var(--band);
  }
  .band__tab {
    position: absolute; right: 0; bottom: 76px; width: 190px; height: 44px;
    background: var(--band);
  }
  .social { position: absolute; left: 50px; bottom: 18px; display: flex; gap: 12px; }
  .social span { width: 38px; height: 38px; border-radius: 50%; background: var(--icon); display: block; }
  .address { position: absolute; left: 168px; bottom: 16px; font-size: 16px; line-height: 22px; color: #1e2a30; }
  .badge {
    position: absolute; right: 40px; bottom: 56px; width: 92px; height: 92px;
    border-radius: 50%; background: var(--badge);
  }
</style>
</head>
<body>

  <section class="card card--front">
    <p class="brand">Meadow's Tail &amp; Kennel</p>
  </section>

  <section class="card card--back">
    <p class="brand">Meadow's Tail &amp; Kennel</p>

    <div class="person">
      <p class="person__name">Marcus Ellery</p>
      <p class="person__title">managing director</p>
    </div>

    <ul class="contacts">
      <li>
        <svg viewBox="0 0 16 16"><circle cx="8" cy="8" r="7.5" fill="var(--ink)"/><path d="M5 4.5l1.6 0 .8 2-1 .8a5 5 0 0 0 2.3 2.3l.8-1 2 .8v1.6c0 .5-.5.8-1 .7A7 7 0 0 1 4.3 5.5c-.1-.5.2-1 .7-1z" fill="#fff"/></svg>
        801-555-0187
      </li>
      <li>
        <svg viewBox="0 0 16 16"><circle cx="8" cy="8" r="7.5" fill="var(--ink)"/><rect x="4" y="5" width="8" height="6" rx="1" fill="#fff"/><path d="M4.3 5.4L8 8.3l3.7-2.9" stroke="var(--ink)" stroke-width="1" fill="none"/></svg>
        thecrew@meadowstailandkennel.example
      </li>
      <li>
        <svg viewBox="0 0 16 16"><circle cx="8" cy="8" r="7.5" fill="var(--ink)"/><circle cx="8" cy="8" r="4.2" fill="none" stroke="#fff" stroke-width="1"/><path d="M3.8 8h8.4M8 3.8c-2 2.4-2 6 0 8.4M8 3.8c2 2.4 2 6 0 8.4" stroke="#fff" stroke-width="1" fill="none"/></svg>
        www.meadowstailandkennel.example
      </li>
    </ul>

    <div class="band__tab"></div>
    <div class="band"></div>
    <div class="badge" role="img" aria-label="Award badge"></div>
    <div class="social" aria-label="Social media">
      <span></span><span></span>
    </div>
    <p class="address">312 W. Larkmoor Avenue<br>Orem UT 84057</p>
  </section>

</body>
</html>
```